Home Page for a Swiss based start up company, trading Natural & Health food ingredients (B2B)

I would like to create a home page for my new start up company (Valtera Swiss AG), the main field of activity is the trading and marketing of Natural and Health food ingredients towards the functional Food and Food supplements industry. (B2B).
Target Market : Functional Food and Food Supplement Manufacturers (B2B) based in Switzerland and Europe
The values I would like to convey are :
- sourcing of natural and health ingredients, (example : natural plant extracts, Omega 3, plant proteins, natural vitamins, vegan food ingredients...etc)
- Health & Nutritional Health
- Eco-friendly and Sustainability
- High Quality Standard in term of products and logistic services
- Trust and reliability
- Flexibility & speed to market
-Technical advice for the development of new products

The site will be translated in 3 languages (German, French, English)
Number of web pages : 5 : Home, About us, Products, Our Services, Contact

See here below attached Logo file.

Here some link of websites which can be taken as benchmark or source of inspiration
- https://quilbamora.com
- https://www.drevilon.com/

Target Market(s)

Manufacturers of Functional Foods and Food Supplements in Switzerland and Europe (B2B)

Industry/Entity Type

B2B Trading of Natural & Health Ingredients

Coding

Coded - Design and coding required

Number of Pages Required

5+ page

Font styles to use
Sans Serif

Colors
0054AA
0677BA
7BADD7
CADEEF
E8F1F8
0094D4
00A9DD
6FCCEA
C7EBF8
E9F6FB
00AB8E
00BBA5
67D7C9
C6EFE9
E9F9F6
59FF00
82FF00
B8FF75
E3FFCB
F4FFEA
FFF300
FFF600
FEFA6F
FFFEC7
FFFEE8
FFC000
F8CF3A
FAE287
FDF2CF
FEFAEE
F0912C
F2A743
F7CA91
FBE8D2
FDF5EE
EE7325
F08F49
F5BC92
FAE3D3
FDF4ED

Requirements
Must have
• inspiration towards nature, sustainability, vegan food, functional food & beverages, food supplements, nutritional health, low carbon footprint
Should not have
• animals, chemistry, food additives

```html
<!DOCTYPE html>
<html lang="en">
<head>
<meta charset="utf-8">
<title>Valtera Swiss AG – Natural &amp; Functional Ingredients Trader</title>
<link href="https://fonts.googleapis.com/css2?family=Outfit:wght@300;400;500;600;700&display=swap" rel="stylesheet">
<style>
:root{
  --red:#d7261b;
  --green:#6f8f0a;
  --green-soft:#eef5cf;
  --ink:#1c1c1c;
  --muted:#6b6b6b;
  --grey-bg:#f1f1f1;
  --news-bg:#f6f6f6;
  --offer-bg:#e8edf1;
  --white:#ffffff;
  --line:#e2e2e2;
  --dark:#232323;
}
*{box-sizing:border-box;margin:0;padding:0}
html,body{width:1200px;height:4000px;overflow:hidden}
body{font-family:"Outfit",sans-serif;color:var(--ink);background:var(--white);position:relative}
.abs{position:absolute}
.center{left:0;width:1200px;text-align:center}
.eyebrow{color:var(--red);font-size:17px;font-weight:400}
.section-title{font-size:44px;font-weight:600;letter-spacing:.5px}
.btn{position:absolute;display:flex;align-items:center;justify-content:center;gap:14px;background:var(--red);color:var(--white);font-weight:600;font-size:19px;border-radius:0 28px 28px 0}
.btn .arrow{width:24px;height:24px;border-radius:50%;background:rgba(255,255,255,.3);display:flex;align-items:center;justify-content:center}
.ph{position:absolute}

.topbar{left:0;top:0;width:1200px;height:24px;background:var(--green);color:#fff;font-size:12px;font-weight:500;padding-left:157px;line-height:24px}
.topbar .soc{position:absolute;top:7px;width:10px;height:10px;border-radius:50%;background:#fff}
.header{left:0;top:24px;width:1200px;height:74px;background:#fff;border-bottom:1px solid var(--line)}
.brand{position:absolute;left:157px;top:22px;display:flex;align-items:center;gap:8px;font-size:24px;font-weight:600;color:var(--green)}
.brand .dot{width:26px;height:26px;border-radius:50%;background:var(--green)}
.nav{position:absolute;left:386px;top:28px;display:flex;gap:24px;font-size:13px}
.nav-div{position:absolute;left:360px;top:0;width:1px;height:74px;background:var(--line)}
.hbtn{position:absolute;top:20px;width:36px;height:36px;border-radius:4px;display:flex;align-items:center;justify-content:center}

.hero{left:0;top:98px;width:1200px;height:539px;background:linear-gradient(180deg,#a9c3d8 0%,#d7e2ea 30%,#6ec5c8 55%,#a7c68a 72%,#f4f3ee 100%)}
.hero-title{top:262px;font-size:56px;font-weight:600;line-height:60px;color:#1b1b1b}
.hero-arrow{position:absolute;top:333px;width:40px;height:40px;border-radius:50%;background:#fff;display:flex;align-items:center;justify-content:center}

.perk{position:absolute;top:679px;width:280px;height:77px;background:var(--green-soft);border-radius:40px 0 0 40px;display:flex;align-items:center;padding-left:20px;gap:18px}
.perk b{display:block;font-size:18px;font-weight:600}
.perk span{font-size:12px;color:var(--muted)}

.values{left:0;top:820px;width:1200px;height:547px;background:var(--grey-bg)}
.pill{position:absolute;width:326px;height:69px;background:#fff;border-radius:35px;display:flex;align-items:center;padding-left:14px;gap:18px;font-size:15px;line-height:20px}
.pill i{width:46px;height:46px;border-radius:50%;border:1px solid var(--line);display:flex;align-items:center;justify-content:center;flex:none}
.pill i:after{content:"";width:28px;height:28px;border-radius:50%;background:var(--c)}

.card-img{position:absolute;top:1530px;width:280px;height:209px}
.tag{position:absolute;top:1719px;height:40px;background:var(--green-soft);border-radius:20px;font-size:17px;display:flex;align-items:center;justify-content:center}

.offer{left:0;top:1927px;width:1200px;height:406px;background:var(--offer-bg)}
.count{position:absolute;top:2125px;width:36px;height:36px;border-radius:50%;background:#fff;display:flex;align-items:center;justify-content:center;font-size:15px}
.count-l{position:absolute;top:2167px;width:80px;text-align:center;font-size:11px;letter-spacing:.5px}

.about p{font-size:14.5px;line-height:22.5px;color:var(--muted);font-weight:300}

.news{left:0;top:2826px;width:1200px;height:691px;background:var(--news-bg)}
.date{position:absolute;top:2990px;width:52px;height:52px;border-radius:50%;background:#fff;font-size:14px;line-height:15px;text-align:center;padding-top:10px;font-weight:500}
.meta{position:absolute;top:3245px;font-size:14px;color:var(--muted)}
.news-title{position:absolute;top:3282px;width:280px;font-size:18px;font-weight:600;line-height:24px}

.foot-ico{position:absolute;left:155px;width:48px;height:48px;border-radius:50%;background:#f0f0f0;display:flex;align-items:center;justify-content:center}
.foot-item{position:absolute;left:224px;font-size:15px;line-height:19px}
.foot-item b{font-weight:600}
.flink{position:absolute;font-size:15px;color:#444}
.fsoc{position:absolute;top:3868px;width:38px;height:38px;border-radius:50%;background:#f0f0f0}
</style>
</head>
<body>

<div class="abs topbar">Welcome to Valtera Swiss AG
  <span class="soc" style="left:928px"></span><span class="soc" style="left:960px"></span><span class="soc" style="left:993px"></span><span class="soc" style="left:1029px"></span>
</div>

<header class="abs header">
  <div class="brand"><span class="dot"></span>Valtera Swiss AG</div>
  <div class="nav-div"></div>
  <nav class="nav"><span>About</span><span>Our Ingredients</span><span>Partners</span><span>News</span><span>Contact</span></nav>
  <div class="hbtn" style="left:879px;background:var(--green-soft)">
    <svg width="16" height="16" viewBox="0 0 16 16" fill="none" stroke="#333" stroke-width="1.5"><circle cx="7" cy="7" r="5"/><path d="M11 11l4 4"/></svg>
  </div>
  <div class="hbtn" style="left:957px;background:#eee">
    <svg width="18" height="18" viewBox="0 0 18 18" fill="none" stroke="#333" stroke-width="1.4"><circle cx="9" cy="9" r="7.5"/><circle cx="9" cy="7" r="2.6"/><path d="M4 14.5c1.5-2.4 8.5-2.4 10 0"/></svg>
  </div>
  <div class="hbtn" style="left:1008px;background:#eee">
    <div role="img" aria-label="English language flag" style="width:20px;height:13px;background:linear-gradient(180deg,#c9333a 0 50%,#eef 50% 100%)"></div>
  </div>
</header>

<section class="abs hero" role="img" aria-label="Alpine lake and snowy mountains with herbs, spices and dropper bottles of plant extracts"></section>
<div class="abs center eyebrow" style="top:224px">100 % Natural Ingredients</div>
<h1 class="abs center hero-title">Natural &amp; Functional<br>Ingredients Trader</h1>
<div class="btn" style="left:498px;top:422px;width:202px;height:56px">Discover Now <span class="arrow"><svg width="12" height="12" viewBox="0 0 12 12" fill="none" stroke="#fff" stroke-width="1.6"><path d="M2 6h8M7 3l3 3-3 3"/></svg></span></div>
<div class="hero-arrow" style="left:53px"><svg width="16" height="16" viewBox="0 0 16 16" fill="none" stroke="#222" stroke-width="1.6"><path d="M14 8H2M6 4L2 8l4 4"/></svg></div>
<div class="hero-arrow" style="left:1106px"><svg width="16" height="16" viewBox="0 0 16 16" fill="none" stroke="#222" stroke-width="1.6"><path d="M2 8h12M10 4l4 4-4 4"/></svg></div>

<div class="perk" style="left:157px">
  <svg width="44" height="44" viewBox="0 0 44 44" fill="none" stroke="#222" stroke-width="1.6"><circle cx="22" cy="22" r="19"/><ellipse cx="22" cy="22" rx="8" ry="19"/><path d="M3 22h38M6 12h32M6 32h32"/></svg>
  <div><b>Worldwide sourcing</b><span>Delivery from just $9.50</span></div>
</div>
<div class="perk" style="left:460px">
  <svg width="40" height="44" viewBox="0 0 40 44" fill="none" stroke="#222" stroke-width="1.6"><circle cx="20" cy="17" r="13"/><circle cx="20" cy="17" r="8"/><path d="M12 28l-5 13 6-3 4 5 3-10M28 28l5 13-6-3-4 5-3-10"/></svg>
  <div><b>Best Quality</b><span>ISO 22000 certified</span></div>
</div>
<div class="perk" style="left:764px">
  <svg width="42" height="44" viewBox="0 0 42 44" fill="none" stroke="#222" stroke-width="1.6"><path d="M5 24v-4a16 16 0 0132 0v4"/><rect x="3" y="22" width="7" height="12" rx="3"/><rect x="32" y="22" width="7" height="12" rx="3"/><path d="M35 34c0 5-6 7-12 7"/></svg>
  <div><b>Expert Support Team</b><span>Customer 48 hours resolve</span></div>
</div>

<section class="abs values"></section>
<div class="abs center eyebrow" style="top:881px">Features</div>
<h2 class="abs center section-title" style="top:903px">Our Values</h2>
<div class="ph" role="img" aria-label="Amber dropper bottle among green leaves and golden softgel capsules" style="left:500px;top:1020px;width:360px;height:347px;background:linear-gradient(180deg,#f1f1f1 0%,#dfe3d6 45%,#c9cfae 100%)"></div>

<div class="pill" style="left:157px;top:986px;--c:#56a93a"><i></i>Sourcing of Natural and<br>Health Ingredients</div>
<div class="pill" style="left:157px;top:1068px;--c:#e0353d"><i></i>Health &amp; Nutritional Health</div>
<div class="pill" style="left:157px;top:1151px;--c:#4fa7d8"><i></i>Eco-friendly and Sustainability</div>
<div class="pill" style="left:157px;top:1233px;--c:#f2a743"><i></i>High Quality Standard in<br>Products and Logistic Services</div>
<div class="pill" style="left:719px;top:986px;--c:#7badd7"><i></i>Trust and Reliability</div>
<div class="pill" style="left:719px;top:1068px;--c:#0677ba"><i></i>Flexibility &amp; Speed to Market</div>
<div class="pill" style="left:719px;top:1151px;--c:#f8cf3a"><i></i>Technical Advice for the<br>Development of New Products</div>
<div class="pill" style="left:719px;top:1233px;--c:#82c341"><i></i>Security of Supply</div>

<div class="abs center eyebrow" style="top:1427px">What We Offer</div>
<h2 class="abs center section-title" style="top:1448px">Our Ingredients</h2>
<div class="card-img" role="img" aria-label="Fresh rosemary sprigs beside a bottle of plant oil" style="left:157px;background:linear-gradient(135deg,#eeeeea,#b9c596 60%,#ddd0a0)"></div>
<div class="card-img" role="img" aria-label="Colourful fruits, berries and vegetables rich in vitamins" style="left:460px;background:linear-gradient(135deg,#b7cf8f,#efb48a 50%,#d98b8f)"></div>
<div class="card-img" role="img" aria-label="Box of dried fruits, nuts and vegan ingredients" style="left:764px;background:linear-gradient(135deg,#f4eee8,#ecc393 55%,#d49a84)"></div>
<div class="tag" style="left:196px;width:202px">Natural Plant Extracts</div>
<div class="tag" style="left:499px;width:202px">Natural Vitamins</div>
<div class="tag" style="left:803px;width:202px">Vegan Ingredients</div>
<div class="btn" style="left:514px;top:1809px;width:172px;height:55px">View All <span class="arrow"><svg width="12" height="12" viewBox="0 0 12 12" fill="none" stroke="#fff" stroke-width="1.6"><path d="M2 6h8M7 3l3 3-3 3"/></svg></span></div>

<section class="abs offer"></section>
<div class="ph" role="img" aria-label="Ripe apricots in a white bowl with green leaves and white blossoms" style="left:668px;top:1927px;width:532px;height:406px;background:linear-gradient(90deg,#e8edf1 0%,#c9d6b8 40%,#9fbb86 75%,#e9c18f 100%)"></div>
<h2 class="abs" style="left:157px;top:1978px;font-size:45px;font-weight:600;line-height:48px">Get 10% off on Natural<br>Anti-oxidants</h2>
<div class="abs eyebrow" style="left:157px;top:2088px">Grab The Offer</div>
<div class="count" style="left:156px">4</div>
<div class="count" style="left:223px">12</div>
<div class="count" style="left:289px">55</div>
<div class="count" style="left:356px">15</div>
<div class="count-l" style="left:134px">DAYS</div>
<div class="count-l" style="left:201px">HOURS</div>
<div class="count-l" style="left:267px">MINUTES</div>
<div class="count-l" style="left:334px">SECONDS</div>
<div class="btn" style="left:157px;top:2218px;width:174px;height:56px">Shop Now <span class="arrow"><svg width="12" height="12" viewBox="0 0 12 12" fill="none" stroke="#fff" stroke-width="1.6"><path d="M2 6h8M7 3l3 3-3 3"/></svg></span></div>

<div class="ph" role="img" aria-label="Hand picking ripe red coffee cherries from a green shrub" style="left:155px;top:2396px;width:399px;height:367px;background:linear-gradient(135deg,#3a6331,#4f7d3a 55%,#6b5a35)"></div>
<section class="about">
  <div class="abs eyebrow" style="left:613px;top:2407px">About Us</div>
  <h2 class="abs" style="left:612px;top:2430px;font-size:44px;font-weight:600;line-height:47px">We Grow Pure,<br>Organic Products</h2>
  <p class="abs" style="left:611px;top:2546px;width:432px">Valtera Swiss AG in Moosbach is a Company limited by shares (AG) from the sector in Trading in food products.The purpose of the company is the production of and trade in food, food additives, raw materials and active ingredients, taking on representations, technical advice and trade.</p>
</section>
<div class="btn" style="left:612px;top:2691px;width:174px;height:56px">Learn More <span class="arrow"><svg width="12" height="12" viewBox="0 0 12 12" fill="none" stroke="#fff" stroke-width="1.6"><path d="M2 6h8M7 3l3 3-3 3"/></svg></span></div>

<section class="abs news"></section>
<div class="abs center eyebrow" style="top:2887px">Articles</div>
<h2 class="abs center section-title" style="top:2910px">Our Latest News</h2>
<div class="ph" role="img" aria-label="Bright orange cordyceps on a wooden board" style="left:155px;top:3017px;width:281px;height:209px;background:linear-gradient(135deg,#a8a8a8,#d98a52 55%,#7a5a3e)"></div>
<div class="ph" role="img" aria-label="Rosemary sprigs with a bowl of extract and oil bottles" style="left:460px;top:3017px;width:281px;height:209px;background:linear-gradient(135deg,#e8e0c8,#a4b073 55%,#c99a52)"></div>
<div class="ph" role="img" aria-label="Bowl of fresh cranberries with green foliage" style="left:764px;top:3017px;width:281px;height:209px;background:linear-gradient(135deg,#f2f2f0,#b8424a 50%,#6c8a56)"></div>
<div class="date" style="left:180px">10<br>Apr</div>
<div class="date" style="left:485px">10<br>Apr</div>
<div class="date" style="left:789px">10<br>Apr</div>
<div class="meta" style="left:155px">By Lena Brunner &nbsp;<span style="color:var(--red)">|</span>&nbsp; 3 Comments</div>
<div class="meta" style="left:460px">By Lena Brunner &nbsp;<span style="color:var(--red)">|</span>&nbsp; 3 Comments</div>
<div class="meta" style="left:764px">By Lena Brunner &nbsp;<span style="color:var(--red)">|</span>&nbsp; 3 Comments</div>
<div class="news-title" style="left:155px">Medicinal Values &amp; Prospect of Cordyceps Extract</div>
<div class="news-title" style="left:460px">Rosemary Extract: Natural Antioxidant and Preservative</div>
<div class="news-title" style="left:764px">Market Segmentation of Cranberry Extract</div>
<svg class="abs" style="left:560px;top:3361px" width="82" height="12"><circle cx="6" cy="6" r="4.5" fill="#bbb"/><circle cx="28" cy="6" r="4.5" fill="#d7261b"/><circle cx="50" cy="6" r="4.5" fill="#bbb"/><circle cx="72" cy="6" r="4.5" fill="#bbb"/></svg>

<div class="abs" style="left:0;top:3517px;width:1200px;height:86px;background:var(--dark)"></div>
<div class="abs" role="img" aria-label="Light green panel with scattered apricots and leaves" style="left:155px;top:3437px;width:890px;height:166px;border-radius:14px;overflow:hidden;background:linear-gradient(90deg,#eef5d4 0%,#f7f9e7 70%,#f3e3c6 100%)">
  <div class="ph" style="left:0;top:0;width:357px;height:166px;background:var(--red);color:#fff;padding:42px 0 0 52px">
    <div style="font-size:16px">Don't Miss Our Deals</div>
    <div style="font-size:34px;font-weight:600;line-height:38px;margin-top:6px">Exclusive Offers<br>&amp; Sale</div>
  </div>
  <div class="ph" style="left:443px;top:40px;font-size:17px;color:#333">Sign up and get a voucher of worth $250.00</div>
  <div class="ph" style="left:426px;top:87px;width:225px;height:44px;background:#fff;border-radius:22px 0 0 22px;font-size:14px;color:#999;padding:13px 0 0 22px">Email address</div>
  <div class="ph" style="left:651px;top:87px;width:168px;height:44px;background:var(--red);border-radius:0 22px 22px 0;color:#fff;font-weight:600;font-size:18px;text-align:center;line-height:44px">Subscribe</div>
</div>

<footer>
  <div class="abs" style="left:155px;top:3645px;width:890px;height:1px;background:var(--line)"></div>
  <div class="abs" style="left:419px;top:3645px;width:1px;height:304px;background:var(--line)"></div>
  <div class="abs" style="left:780px;top:3645px;width:1px;height:304px;background:var(--line)"></div>

  <div class="foot-ico" style="top:3703px"><svg width="20" height="16" viewBox="0 0 20 16" fill="none" stroke="#333" stroke-width="1.4"><rect x="1" y="1" width="18" height="14" rx="2"/><path d="M1 2l9 7 9-7"/></svg></div>
  <div class="foot-item" style="top:3707px"><b>Email</b><br>info@valteraswiss.com</div>
  <div class="foot-ico" style="top:3774px"><svg width="18" height="18" viewBox="0 0 18 18" fill="none" stroke="#333" stroke-width="1.4"><path d="M4 1l3 4-2 2c1 2 4 5 6 6l2-2 4 3-2 3C8 17 1 10 1 3z"/></svg></div>
  <div class="foot-item" style="top:3778px"><b>Phone</b><br>020.4.118.362</div>
  <div class="foot-ico" style="top:3846px"><svg width="16" height="20" viewBox="0 0 16 20" fill="none" stroke="#333" stroke-width="1.4"><path d="M8 19s7-7 7-11A7 7 0 001 8c0 4 7 11 7 11z"/><circle cx="8" cy="8" r="2.5"/></svg></div>
  <div class="foot-item" style="top:3850px"><b>Address</b><br>Rennweg 14, 8612<br>Moosbach, Switzerland</div>

  <div class="abs" style="left:420px;width:360px;top:3700px;display:flex;justify-content:center;align-items:center;gap:10px;font-size:27px;font-weight:600;color:var(--ink)"><span style="width:28px;height:28px;border-radius:50%;background:var(--ink)"></span>Valtera Swiss AG</div>
  <p class="abs" style="left:445px;top:3780px;width:310px;text-align:center;font-size:14.5px;line-height:21px;color:#555;font-weight:300">Valtera Swiss AG in Moosbach is a Company limited by shares (AG) from the sector in Trading in food products.</p>
  <div class="fsoc" style="left:498px"></div><div class="fsoc" style="left:554px"></div><div class="fsoc" style="left:610px"></div><div class="fsoc" style="left:666px"></div>

  <div class="abs" style="left:821px;top:3705px;font-size:16px;font-weight:600">Important Links</div>
  <div class="flink" style="left:821px;top:3749px">About</div>
  <div class="flink" style="left:821px;top:3785px">Our Ingredients</div>
  <div class="flink" style="left:821px;top:3821px">Partners</div>
  <div class="flink" style="left:821px;top:3857px">News</div>
  <div class="flink" style="left:821px;top:3892px">Contact</div>
  <div class="flink" style="left:966px;top:3749px">Account</div>
  <div class="flink" style="left:966px;top:3785px">Help</div>
  <div class="flink" style="left:966px;top:3821px">Support</div>
  <div class="flink" style="left:966px;top:3857px">FAQ</div>

  <div class="abs" style="left:155px;top:3949px;width:890px;height:1px;background:var(--line)"></div>
  <div class="abs center" style="top:3964px;font-size:14px;color:#444">© Copyright 2022 Valtera Swiss AG. All Rights Reserved.</div>
</footer>

</body>
</html>
```